Olvar business stationery
Purified water company
Simple
Rodrigo Lemus
Gerente General
Calle 38 con Avenida Tzabalché
entre 164 y 166
Colonia Vista de Orquídeas
Mérida, Yucatán
rlem@purificadoraolvar-mx.com
www.purificadoraolvar-mx.com
- The logo font is Quadranta
- We would like all stationary, including letterhead, envelopes, business card, presentation folder, compliment card and fax cover
- Color gradient of blue
Light blue C=50 M=1 Y=0 K=0
Blue C=92 M=63 Y=1 K=0
Stroke light blue C=27 M=0 Y=1 K=0
siempre contigo...
- Name and image should be integrated in the design of the stationary
- Designers can split the name (quadranta font) and the waterfall image to use as they like during their designs

```html
<!DOCTYPE html>
<html lang="es">
<head>
<meta charset="utf-8">
<title>Olvar business stationery – business card</title>
<link rel="stylesheet" href="https://fonts.googleapis.com/css2?family=Arimo:wght@400;700&display=swap">
<style>
  :root {
    --page-bg: #e9e6df;
    --card-bg: #ffffff;
    --brand-blue: #1862ad;
    --brand-light-blue: #7fcdf4;
    --brand-pale-blue: #c4e9fa;
    --brand-green: #86b92a;
    --text-dark: #2a2a2a;
    --icon-blue: #1f6fb8;
  }
  * { box-sizing: border-box; margin: 0; padding: 0; }
  html, body {
    width: 1200px; height: 778px; overflow: hidden;
    background: var(--page-bg);
    font-family: "Arimo", Arial, sans-serif;
  }
  .business-card {
    position: absolute; left: 60px; top: 85px;
    width: 1080px; height: 608px;
    background: var(--card-bg);
    box-shadow: 0 4px 14px rgba(0,0,0,0.18);
    overflow: hidden;
  }
  .side-band {
    position: absolute; left: 0; top: 0; bottom: 0; width: 78px;
    background: linear-gradient(90deg, var(--brand-light-blue) 0%, var(--brand-blue) 100%);
  }
  .side-stripe {
    position: absolute; left: 88px; top: 0; bottom: 0; width: 10px;
    background: var(--brand-green);
  }
  .logo-illustration {
    position: absolute; left: 262px; top: 42px; width: 168px; height: 168px;
  }
  .brand-name {
    position: absolute; left: 140px; top: 196px;
    font-size: 120px; font-weight: 400; line-height: 1;
    color: var(--brand-light-blue);
    letter-spacing: 2px;
  }
  .address {
    position: absolute; left: 146px; top: 345px;
    font-size: 22px; line-height: 28px; color: var(--text-dark);
    font-style: normal;
  }
  .contact-list {
    position: absolute; left: 146px; top: 478px;
    list-style: none;
    font-size: 22px; line-height: 31px; color: var(--text-dark);
  }
  .contact-list li { display: flex; align-items: center; gap: 12px; }
  .contact-list svg { width: 18px; height: 18px; flex: none; }
  .person {
    position: absolute; left: 640px; top: 52px; width: 400px;
    text-align: center;
  }
  .person-name {
    font-size: 34px; font-weight: 700; color: var(--brand-blue);
  }
  .person-title {
    margin-top: 8px;
    font-size: 27px; font-weight: 400; color: var(--brand-green);
  }
  .decor-illustration {
    position: absolute; left: 665px; top: 215px; width: 410px; height: 380px;
  }
</style>
</head>
<body>
  <article class="business-card">
    <div class="side-band"></div>
    <div class="side-stripe"></div>

    <svg class="logo-illustration" viewBox="0 0 168 168" role="img" aria-label="Waterfall with trees and leaves illustration">
      <defs>
        <radialGradient id="logoFill" cx="50%" cy="45%" r="55%">
          <stop offset="0%" stop-color="#eaf7fd"/>
          <stop offset="60%" stop-color="#9fd9f4"/>
          <stop offset="100%" stop-color="#8bbf5a"/>
        </radialGradient>
      </defs>
      <circle cx="84" cy="84" r="80" fill="url(#logoFill)"/>
    </svg>

    <div class="brand-name">Olvar</div>

    <address class="address">
      Calle 38 con Avenida Tzabalché<br>
      entre 164 y 166<br>
      Colonia Vista de Orquídeas<br>
      Mérida, Yucatán
    </address>

    <ul class="contact-list">
      <li>
        <svg viewBox="0 0 18 18"><rect x="4" y="1" width="10" height="16" rx="2" fill="var(--icon-blue)"/><rect x="6" y="3" width="6" height="9" fill="#fff"/></svg>
        999-4817263
      </li>
      <li>
        <svg viewBox="0 0 18 18"><rect x="1" y="4" width="16" height="11" rx="1" fill="none" stroke="var(--icon-blue)" stroke-width="2"/><path d="M1 5 L9 11 L17 5" fill="none" stroke="var(--icon-blue)" stroke-width="2"/></svg>
        rlem@purificadoraolvar-mx.com
      </li>
      <li>
        <svg viewBox="0 0 18 18"><circle cx="9" cy="9" r="8" fill="var(--icon-blue)"/><path d="M1 9 H17 M9 1 C5 5 5 13 9 17 M9 1 C13 5 13 13 9 17" fill="none" stroke="#fff" stroke-width="1.3"/></svg>
        www.purificadoraolvar-mx.com
      </li>
    </ul>

    <div class="person">
      <div class="person-name">Rodrigo Lemus</div>
      <div class="person-title">Gerente General</div>
    </div>

    <svg class="decor-illustration" viewBox="0 0 410 380" role="img" aria-label="Faint waterfall with trees and leaves illustration">
      <defs>
        <radialGradient id="decorFill" cx="50%" cy="40%" r="60%">
          <stop offset="0%" stop-color="#f4fbfe"/>
          <stop offset="65%" stop-color="#d6eff9"/>
          <stop offset="100%" stop-color="#e6efd2"/>
        </radialGradient>
      </defs>
      <circle cx="205" cy="190" r="175" fill="url(#decorFill)" opacity="0.85"/>
    </svg>
  </article>
</body>
</html>
```